依頼詳細
エステサロン、SPA施設、百貨店、雑貨屋などの店頭でも陳列できるようなシンプルかつおしゃれで女性に好感が持てるようなデザインを希望します。
またホームセンターやドラックストアなどで販売されているような商品に比べて高価になる為、高級感があるデザインを希望します。

シリカは水晶(クリスタル)から抽出しているので、水晶のマーク、イラストなどを入れたいです。
本製品は、雑貨ではなく「化粧品」としての販売となります。

ミストヘイヴンと水晶の写真は添付資料をご確認ください。
記載項目
ボトルサイズD78㎜×H160㎜(添付参照)
印刷:4C
材質:シュリンクフィルムPP
希望イメージ
シンプル 複雑
単色 カラフル
暗い 明るい
日常 高級
遊び心 厳粛
未来的 伝統的
女性的 男性的
希望する色
青系、水色系
納品ファイル
• 高解像度JPG (.jpg)
• イラストレーター形式 (.ai)
補足説明
変更で申し訳ございませんが、
水晶(シリカ)のロゴはなしでお願いいたします。
アイスランドにあるミストヘイヴンのイメージで
高級感のあるデザインを希望します。
よろしくお願いいたします。
■ 選んだ理由

ミストヘイヴンのイメージが湧きやすくイメージに近かったため選ばせて頂きました。

■ 提案者全員のお礼・コメント

この度はたくさんのご提案を頂戴し誠にありがとうございました。
どれも素敵なデザインで選定に悩みました。
また機会があればご参加いただけますと幸いです。
この度はありがとうございました。

```html
<!DOCTYPE html>
<html lang="ja">
<head>
<meta charset="utf-8">
<title>Quarta Nimbus – ボトルラベル</title>
<link rel="stylesheet" href="https://fonts.googleapis.com/css2?family=Cinzel:wght@400&display=swap">
<style>
  :root {
    --lagoon-turquoise: #3fc3c9;
    --lagoon-aqua: #5fd6d3;
    --lagoon-deep: #2aa3b8;
    --mist-violet: #6b5bb0;
    --mist-lilac: #8a7cc8;
    --frost-white: #ffffff;
    --label-w: 1200px;
    --label-h: 2452px;
  }
  html, body {
    margin: 0;
    padding: 0;
    width: var(--label-w);
    height: var(--label-h);
    overflow: hidden;
    background: var(--lagoon-turquoise);
  }
  .label {
    position: relative;
    width: var(--label-w);
    height: var(--label-h);
    overflow: hidden;
    background:
      radial-gradient(ellipse 520px 700px at 260px 1100px, rgba(107, 91, 176, 0.85), rgba(107, 91, 176, 0) 70%),
      radial-gradient(ellipse 420px 520px at 620px 700px, rgba(138, 124, 200, 0.6), rgba(138, 124, 200, 0) 70%),
      radial-gradient(ellipse 700px 500px at 200px 1900px, rgba(255, 255, 255, 0.35), rgba(255, 255, 255, 0) 70%),
      radial-gradient(ellipse 600px 800px at 1050px 300px, rgba(95, 214, 211, 0.8), rgba(95, 214, 211, 0) 70%),
      linear-gradient(170deg, var(--lagoon-aqua) 0%, var(--lagoon-turquoise) 45%, var(--lagoon-deep) 100%);
  }
  .watercolor-texture,
  .product-name {
    position: absolute;
    inset: 0;
  }
  .product-name__text {
    font-family: "Cinzel", serif;
    font-weight: 400;
    fill: var(--frost-white);
  }
  .crystal-illustration {
    position: absolute;
    left: 300px;
    top: 1500px;
    width: 600px;
    height: 380px;
    border-radius: 40px;
    background: radial-gradient(ellipse at center, rgba(255, 255, 255, 0.28), rgba(255, 255, 255, 0.05) 75%);
  }
  .base-band {
    position: absolute;
    left: 0;
    right: 0;
    top: 2020px;
    height: 68px;
    background: var(--frost-white);
  }
</style>
</head>
<body>
  <main class="label">
    <svg class="watercolor-texture" width="1200" height="2452" viewBox="0 0 1200 2452" aria-hidden="true">
      <g fill="#ffffff" opacity="0.35">
        <circle cx="140" cy="220" r="3"/>
        <circle cx="980" cy="420" r="2.5"/>
        <circle cx="760" cy="180" r="2"/>
        <circle cx="1080" cy="900" r="3"/>
        <circle cx="90" cy="1420" r="2"/>
        <circle cx="1020" cy="1660" r="2.5"/>
        <circle cx="420" cy="2260" r="2"/>
        <circle cx="900" cy="2330" r="3"/>
      </g>
    </svg>

    <svg class="product-name" width="1200" height="2452" viewBox="0 0 1200 2452" role="img" aria-label="QUARTA NIMBUS">
      <text class="product-name__text" x="90" y="1020" font-size="280" textLength="1020" lengthAdjust="spacingAndGlyphs">QUARTA</text>
      <text class="product-name__text" x="80" y="1320" font-size="245" textLength="1040" lengthAdjust="spacingAndGlyphs">NIMBUS</text>
    </svg>

    <div class="crystal-illustration" role="img" aria-label="白い線で描かれた水晶クラスターのイラスト"></div>

    <div class="base-band"></div>
  </main>
</body>
</html>
```